Bakery looking for new Business cards

I have a new logo and now its time to upgrade our business cards.
e-mail - info@corwelbakehouse.com
www.corwelbakehouse.com
318-547-2096

418e Pell Creek rd. Bloomingdale IL 60108
Bakery Hour's Tuesday-Saturday 8am-5pm

Industry/Entity Type

Bakery

Contact Information for Business Card

Hr's

Requirements
Must have
• Business information.
Nice to have
• would like to include a QR code for our website.

```html
<!DOCTYPE html>
<html lang="en">
<head>
<meta charset="utf-8">
<title>Corwel Bakehouse – Business Cards</title>
<link rel="stylesheet" href="https://fonts.googleapis.com/css2?family=Lobster&family=Mulish:wght@400;600&display=swap">
<style>
  :root {
    --page-bg: #ece8e2;
    --card-dark: #1d1d1e;
    --gold: #e8b351;
    --ink: #2a2623;
    --paper-white: #f1f1f1;
    --text-light: #e6e6e6;
  }
  * { margin: 0; padding: 0; box-sizing: border-box; }
  html, body { width: 1200px; height: 780px; overflow: hidden; }
  body {
    background: var(--page-bg);
    font-family: "Mulish", sans-serif;
    position: relative;
  }
  .card {
    position: absolute;
    top: 236px;
    width: 540px;
    height: 309px;
    border-radius: 3px;
    overflow: hidden;
    box-shadow: 0 10px 24px rgba(0,0,0,0.18);
  }
  /* Front */
  .card-front { left: 40px; background: var(--card-dark); color: var(--text-light); }
  .holder-name {
    position: absolute; left: 40px; top: 40px;
    font-family: "Lobster", cursive; font-size: 36px; font-weight: 400; color: var(--gold);
    line-height: 1;
  }
  .holder-title { position: absolute; left: 40px; top: 84px; font-size: 16px; color: var(--text-light); }
  .divider {
    position: absolute; left: 40px; right: 40px; top: 130px;
    height: 2px; background: var(--gold);
  }
  .contact-list { position: absolute; left: 40px; top: 150px; list-style: none; }
  .contact-list li {
    display: flex; align-items: center; gap: 10px;
    font-size: 14px; line-height: 24px; color: var(--text-light);
  }
  .contact-list svg { width: 12px; height: 12px; fill: var(--gold); flex: none; }
  .brand {
    position: absolute; right: 40px; top: 56px;
    display: flex; align-items: center; gap: 10px;
  }
  .brand-mark { width: 18px; height: 18px; border-radius: 50%; background: var(--gold); }
  .brand-name { font-size: 20px; font-weight: 600; color: var(--text-light); }
  .address {
    position: absolute; right: 40px; top: 160px;
    font-size: 15px; line-height: 24px; color: var(--text-light);
  }
  .edge-band { position: absolute; left: 0; bottom: 0; width: 540px; height: 10px; }
  /* Back */
  .card-back { left: 620px; background: var(--gold); color: var(--ink); }
  .card-back .brand-back {
    position: absolute; left: 0; right: 0; top: 110px;
    display: flex; justify-content: center; align-items: center; gap: 12px;
  }
  .card-back .brand-mark { width: 24px; height: 24px; background: var(--ink); }
  .card-back .brand-name { font-size: 28px; color: var(--ink); }
  .hours {
    position: absolute; left: 0; right: 0; top: 190px;
    text-align: center; font-size: 15px; color: var(--ink);
  }
</style>
</head>
<body>

<section class="card card-front" aria-label="Business card front">
  <h1 class="holder-name">Daniel Brooke</h1>
  <p class="holder-title">Founder &amp; CEO</p>

  <div class="brand">
    <span class="brand-mark"></span>
    <span class="brand-name">Corwel Bakehouse</span>
  </div>

  <div class="divider"></div>

  <ul class="contact-list">
    <li>
      <svg viewBox="0 0 12 12" aria-hidden="true"><path d="M2.5 0.8l2 2.2-1 1.3c.6 1.4 1.8 2.6 3.2 3.2l1.3-1 2.2 2-1 2c-4.6-.3-8.3-4-8.7-8.7z"/></svg>
      318-547-2096
    </li>
    <li>
      <svg viewBox="0 0 12 12" aria-hidden="true"><path d="M0.5 2.5h11v7h-11z M1 3l5 3.6L11 3v.9L6 7.5 1 3.9z" fill-rule="evenodd"/></svg>
      info@corwelbakehouse.com
    </li>
    <li>
      <svg viewBox="0 0 12 12" aria-hidden="true"><circle cx="6" cy="6" r="5.5"/></svg>
      corwelbakehouse.com
    </li>
  </ul>

  <p class="address">418e Pell Creek Rd<br>Marlowe Falls, IL 60412</p>

  <svg class="edge-band" viewBox="0 0 540 10" preserveAspectRatio="none" aria-hidden="true">
    <rect x="0" y="0" width="540" height="10" fill="var(--paper-white)"/>
    <polygon points="0,0 352,0 344,10 0,10" fill="var(--gold)"/>
  </svg>
</section>

<section class="card card-back" aria-label="Business card back">
  <div class="brand brand-back">
    <span class="brand-mark"></span>
    <span class="brand-name">Corwel Bakehouse</span>
  </div>
  <p class="hours">Bakery Hour's Tuesday-Saturday 8am-5pm</p>
</section>

</body>
</html>
```